" é uma empresa produtora de polpas de frutas congeladas, sumos naturais, e gelados artesanais. comercialisamos os produtos para pessoas individuais , lojas, restaurants e eventos. funcianamento: a materia prima (fruta) chega a fabrica, e é processeda segungo um protocolo definido pelas normas de saude e higiene. posterioremente é embalado e armazenado. os pedidos dos clientes chegam por telefone ou whatsaap e nós procedemos de acordo. fazemos entregas ou o cliente vem a loja. em junho sera aberta a loja/restaurante/gelataria fisica. todos os products são processados por nós. usamos produtos de qualidade, sem corantes e sem conservantes artificiais. "

```html
<!DOCTYPE html>
<html lang="pt">
<head>
<meta charset="utf-8">
<title>Frutaria Mukua — Pasta Institucional</title>
<link href="https://fonts.googleapis.com/css2?family=Montserrat:wght@400;600&family=Kaushan+Script&display=swap" rel="stylesheet">
<style>
  :root{
    --bg:#efe9e1;
    --wine:#7b111a;
    --wine-deep:#560a10;
    --wine-band:#8e1520;
    --gold:#f0a81c;
    --paper:#ffffff;
    --cream:#f7ece0;
  }
  *{box-sizing:border-box;margin:0;padding:0}
  html,body{width:1200px;height:1200px;overflow:hidden;background:var(--bg)}
  body{position:relative;font-family:"Montserrat",sans-serif}

  .spread{position:absolute;left:240px;width:720px;height:500px;display:flex;box-shadow:0 10px 30px rgba(60,20,10,.25)}
  .spread--outside{top:60px}
  .spread--inside{top:640px}

  .panel{position:relative;width:360px;height:500px;overflow:hidden}
  .spread--outside .panel + .panel{border-left:1px solid rgba(0,0,0,.25)}
  .spread--inside .panel + .panel{border-left:1px solid #ddd}

  .cover-photo{position:absolute;inset:0;
    background:radial-gradient(ellipse at 55% 35%, #8c1a22 0%, var(--wine) 45%, var(--wine-deep) 100%)}

  .brand-name{font-family:"Montserrat",sans-serif;font-weight:600;color:var(--paper);font-size:24px;letter-spacing:.5px;white-space:nowrap;line-height:1}

  .back .brand-name{position:absolute;left:28px;top:262px}
  .front .brand-name{position:absolute;right:30px;top:225px}
  .tagline{position:absolute;right:30px;top:272px;font-family:"Kaushan Script",cursive;color:var(--gold);font-size:28px;line-height:1}

  .contact-band{position:absolute;left:0;right:0;bottom:0;height:80px;background:var(--wine-band);padding:12px 22px;display:flex;flex-direction:column;gap:5px}
  .contact{display:flex;align-items:center;gap:7px;color:var(--cream);font-size:9.5px;line-height:1.2}
  .contact svg{width:10px;height:10px;flex:none;fill:var(--gold)}
  .socials{position:absolute;left:22px;top:-22px;display:flex;gap:16px;color:var(--cream);font-size:9px}

  .inner-sheet{position:absolute;inset:0;background:var(--paper)}
  .pocket{position:absolute;left:0;right:0;bottom:0;height:190px;overflow:hidden}
  .pocket-photo{position:absolute;inset:0;background:linear-gradient(100deg,var(--wine-deep) 0%,var(--wine) 55%,#9a2a2a 100%)}
  .pocket .brand-name{position:absolute;font-size:22px}
  .pocket--left .brand-name{left:50%;top:84px;transform:translateX(-50%)}
  .pocket--right .brand-name{right:22px;top:30px}
  .pocket-contacts{position:absolute;left:20px;top:82px;display:flex;flex-direction:column;gap:6px}
</style>
</head>
<body>

<section class="spread spread--outside" aria-label="Capa e contracapa da pasta">
  <div class="panel back">
    <div class="cover-photo" role="img" aria-label="Fotografia em tons de vinho de um embondeiro (baobá) na savana"></div>
    <span class="brand-name">Frutaria Mukua</span>
    <div class="contact-band">
      <div class="socials"><span>/frutariamukua</span><span>/frutariamukua</span></div>
      <div class="contact"><svg viewBox="0 0 10 10"><path d="M5 0a3.5 3.5 0 0 0-3.5 3.5C1.5 6 5 10 5 10s3.5-4 3.5-6.5A3.5 3.5 0 0 0 5 0zm0 5a1.5 1.5 0 1 1 0-3 1.5 1.5 0 0 1 0 3z"/></svg><span>Rua das Mangueiras, 120 – Loja 3<br>Luanda – Angola | NIF 5000000000</span></div>
      <div class="contact"><svg viewBox="0 0 10 10"><path d="M2 0l2 2.2-1 1.3a6 6 0 0 0 3.5 3.5l1.3-1L10 8l-1.5 2C4 10 0 6 0 1.5z"/></svg><span>(+244) 900 000 000</span></div>
      <div class="contact"><svg viewBox="0 0 10 10"><circle cx="5" cy="5" r="4.5" fill="none" stroke="#f0a81c" stroke-width="1"/><path d="M.5 5h9M5 .5v9" stroke="#f0a81c" stroke-width=".8"/></svg><span>www.frutariamukua.ao</span></div>
    </div>
  </div>
  <div class="panel front">
    <div class="cover-photo" role="img" aria-label="Continuação da fotografia do embondeiro em tons de vinho"></div>
    <span class="brand-name">Frutaria Mukua</span>
    <div class="tagline">Fruta Pura</div>
  </div>
</section>

<section class="spread spread--inside" aria-label="Interior da pasta com bolsas">
  <div class="panel">
    <div class="inner-sheet"></div>
    <div class="pocket pocket--left">
      <div class="pocket-photo" role="img" aria-label="Fotografia de frutas tropicais em tons de vinho"></div>
      <span class="brand-name">Frutaria Mukua</span>
    </div>
  </div>
  <div class="panel">
    <div class="inner-sheet"></div>
    <div class="pocket pocket--right">
      <div class="pocket-photo" role="img" aria-label="Fotografia de frutas tropicais em tons de vinho"></div>
      <span class="brand-name">Frutaria Mukua</span>
      <div class="pocket-contacts">
        <div class="contact"><svg viewBox="0 0 10 10"><path d="M5 0a3.5 3.5 0 0 0-3.5 3.5C1.5 6 5 10 5 10s3.5-4 3.5-6.5A3.5 3.5 0 0 0 5 0zm0 5a1.5 1.5 0 1 1 0-3 1.5 1.5 0 0 1 0 3z"/></svg><span>Rua das Mangueiras, 120 – Loja 3<br>Luanda – Angola</span></div>
        <div class="contact"><svg viewBox="0 0 10 10"><path d="M2 0l2 2.2-1 1.3a6 6 0 0 0 3.5 3.5l1.3-1L10 8l-1.5 2C4 10 0 6 0 1.5z"/></svg><span>(+244) 900 000 000</span></div>
        <div class="contact"><svg viewBox="0 0 10 10"><circle cx="5" cy="5" r="4.5" fill="none" stroke="#f0a81c" stroke-width="1"/><path d="M.5 5h9M5 .5v9" stroke="#f0a81c" stroke-width=".8"/></svg><span>www.frutariamukua.ao</span></div>
      </div>
    </div>
  </div>
</section>

</body>
</html>
```